Create a professional, eye-catching business card design that reflects the values and services of Brookfern Veterinary Hospital. we provide veterinary services and the business card should be a memorable representation of the clinic and align with its branding and mission. our tag line is "Kind Care for Every Paw, Every Day"
Use clean, modern typography. Prioritize readability and professionalism. We would like to see designs that use the color blue, as in the logo example. the final design should communicate professionalism and care, with attention to detail.

```html
<!DOCTYPE html>
<html lang="en">
<head>
<meta charset="utf-8">
<title>Brookfern Veterinary Hospital – Business Card</title>
<link rel="stylesheet" href="https://fonts.googleapis.com/css2?family=Montserrat:wght@700&family=Roboto:wght@400;500;700&display=swap">
<style>
  :root {
    --navy: #1e2f62;
    --navy-ink: #1f2f5c;
    --amber: #f0a830;
    --tagline: #f2a533;
    --white: #ffffff;
    --backdrop: #e4e2e3;
  }
  * { margin: 0; padding: 0; box-sizing: border-box; }
  html, body { width: 1200px; height: 1200px; overflow: hidden; background: var(--backdrop); }
  .canvas { position: relative; width: 1200px; height: 1200px; }

  .card {
    position: absolute;
    left: 185px;
    width: 857px;
    height: 486px;
    overflow: hidden;
  }
  .card--front { top: 92px; background: var(--navy); }
  .card--back { top: 629px; background: var(--navy); }

  .brand {
    position: absolute;
    display: flex;
    flex-direction: column;
    align-items: center;
    color: var(--white);
    font-family: "Montserrat", sans-serif;
    font-weight: 700;
    text-align: center;
  }
  .brand__circle {
    border: 2px solid var(--white);
    border-radius: 50%;
  }
  .brand__name { line-height: 1; letter-spacing: 0.5px; }
  .brand__sub { line-height: 1; letter-spacing: 0.6px; }

  .card--front .brand { left: 0; right: 0; top: 106px; }
  .card--front .brand__circle { width: 150px; height: 150px; margin-bottom: 18px; }
  .card--front .brand__name { font-size: 52px; }
  .card--front .brand__sub { font-size: 19px; margin-top: 6px; }

  .tagline {
    margin-top: 10px;
    color: var(--tagline);
    font-family: "Roboto", sans-serif;
    font-weight: 700;
    font-size: 24px;
    letter-spacing: 0.3px;
    white-space: nowrap;
  }

  .card--back .brand { left: 0; width: 406px; top: 126px; }
  .card--back .brand__circle { width: 150px; height: 150px; margin-bottom: 16px; }
  .card--back .brand__name { font-size: 46px; }
  .card--back .brand__sub { font-size: 17px; margin-top: 5px; }

  .contact-panel {
    position: absolute;
    left: 406px;
    top: 0;
    width: 451px;
    height: 486px;
    background: var(--amber);
    font-family: "Roboto", sans-serif;
    color: var(--navy-ink);
  }
  .person { position: absolute; left: 82px; top: 126px; }
  .person__name { font-size: 29px; font-weight: 700; letter-spacing: 0.6px; line-height: 1; }
  .person__role { font-size: 18px; font-weight: 400; letter-spacing: 0.8px; margin-top: 6px; }

  .contact-list { position: absolute; left: 86px; top: 202px; list-style: none; }
  .contact-list li {
    display: flex;
    align-items: flex-start;
    gap: 14px;
    font-size: 18px;
    font-weight: 700;
    letter-spacing: 0.3px;
    line-height: 26px;
    margin-bottom: 11px;
    white-space: nowrap;
  }
  .contact-list svg { width: 22px; height: 22px; flex: none; margin-top: 2px; }
</style>
</head>
<body>
<main class="canvas">

  <section class="card card--front" aria-label="Card front">
    <div class="brand">
      <div class="brand__circle"></div>
      <div class="brand__name">BROOKFERN</div>
      <div class="brand__sub">VETERINARY HOSPITAL</div>
      <p class="tagline">Kind Care for Every Paw, Every Day</p>
    </div>
  </section>

  <section class="card card--back" aria-label="Card back">
    <div class="brand">
      <div class="brand__circle"></div>
      <div class="brand__name">BROOKFERN</div>
      <div class="brand__sub">VETERINARY HOSPITAL</div>
    </div>

    <div class="contact-panel" role="img" aria-label="Amber panel with a soft pattern of paw prints, bones and hearts">
      <div class="person">
        <div class="person__name">DANA REYES</div>
        <div class="person__role">DIRECTOR</div>
      </div>
      <ul class="contact-list">
        <li>
          <svg viewBox="0 0 22 22" aria-hidden="true"><rect width="22" height="22" rx="4" fill="var(--navy-ink)"/><path d="M7 5.5c1 0 1.6 2.4 1.2 3-.4.5-1 .7-.6 1.6.6 1.3 1.8 2.5 3 3 .9.4 1.1-.2 1.6-.6.6-.4 3 .2 3 1.2 0 1.3-1.4 2.3-2.6 2-3.6-.8-6.6-3.8-7.4-7.4C4.9 7 5.8 5.5 7 5.5z" fill="var(--amber)"/></svg>
          <span>5550142876</span>
        </li>
        <li>
          <svg viewBox="0 0 22 22" aria-hidden="true"><rect width="22" height="22" rx="4" fill="var(--navy-ink)"/><rect x="4.5" y="6.5" width="13" height="9" fill="none" stroke="var(--amber)" stroke-width="1.6"/><path d="M4.5 6.5l6.5 5 6.5-5" fill="none" stroke="var(--amber)" stroke-width="1.6"/></svg>
          <span>care@brookfernvet.com</span>
        </li>
        <li>
          <svg viewBox="0 0 22 22" aria-hidden="true"><rect width="22" height="22" rx="4" fill="var(--navy-ink)"/><circle cx="11" cy="11" r="6" fill="none" stroke="var(--amber)" stroke-width="1.6"/><path d="M5 11h12M11 5c-2.4 3.4-2.4 8.6 0 12M11 5c2.4 3.4 2.4 8.6 0 12" fill="none" stroke="var(--amber)" stroke-width="1.3"/></svg>
          <span>www.brookfernvet.com</span>
        </li>
        <li>
          <svg viewBox="0 0 22 22" aria-hidden="true"><rect width="22" height="22" rx="4" fill="var(--navy-ink)"/><path d="M11 4.5a4.8 4.8 0 0 0-4.8 4.8c0 3.4 4.8 8.2 4.8 8.2s4.8-4.8 4.8-8.2A4.8 4.8 0 0 0 11 4.5z" fill="var(--amber)"/><circle cx="11" cy="9.3" r="1.8" fill="var(--navy-ink)"/></svg>
          <span>48 Mill Lane,<br>Fernvale, ST 20417</span>
        </li>
      </ul>
    </div>
  </section>

</main>
</body>
</html>
```